Alloy wheel repair business needs a website

Install logo previously purchased from pixelbazaar, toolbar with dropdowns. services, gallery, clients , contact ect
Maybe mission statment

Target Market(s)

vehicle owners, auto dealers,insurance companies,

Industry/Entity Type

Alloy Wheel Repair

Coding

Coded - Design and coding required

Number of Pages Required

4 page

Font styles to use
Sans Serif

Colors
0054AA
0677BA
7BADD7
CADEEF
E8F1F8

```html
<!DOCTYPE html>
<html lang="en">
<head>
<meta charset="UTF-8">
<title>Rimcraft Works – Wheel Repairs Specialists</title>
<link href="https://fonts.googleapis.com/css2?family=Audiowide&family=Montserrat:ital,wght@0,400;0,500;0,600;0,700;0,800;1,400;1,700&display=swap" rel="stylesheet">
<style>
:root{
  --blue-deep:#0054AA;
  --blue:#0677BA;
  --blue-bright:#2F7FD0;
  --blue-hero:#3F88D2;
  --blue-soft:#7BADD7;
  --blue-pale:#CADEEF;
  --blue-mist:#E8F1F8;
  --ink:#1E1F27;
  --ink-2:#26272F;
  --text:#3A3A3A;
  --muted:#6E6E78;
  --white:#FFFFFF;
  --star:#F4B400;
}
*{box-sizing:border-box;margin:0;padding:0}
html,body{width:1200px;height:5059px;overflow:hidden}
body{font-family:'Montserrat',sans-serif;color:var(--text);background:var(--white);position:relative}
.abs{position:absolute}
section,header,footer{position:absolute;left:0;width:1200px;overflow:hidden}
.display{font-family:'Audiowide',sans-serif;font-style:italic;color:var(--blue-bright);text-transform:uppercase;letter-spacing:1px;z-index:2}
.num{font-family:'Audiowide',sans-serif;font-style:italic;font-size:58px;color:transparent;-webkit-text-stroke:1.4px #9a9aa3;line-height:1}
.label{font-family:'Montserrat',sans-serif;font-weight:800;font-style:italic;font-size:12px;letter-spacing:1px;text-transform:uppercase;z-index:2}
.photo{position:absolute;overflow:hidden}
.btn{position:absolute;display:flex;align-items:center;justify-content:center;gap:8px;font-weight:700;font-size:15px;color:var(--white);text-decoration:none;z-index:1}
.btn::before{content:"";position:absolute;inset:0;background:var(--blue-bright);transform:skewX(-22deg);z-index:-1}
.btn::after{content:"";position:absolute;inset:0;border:1.5px solid var(--blue-bright);transform:skewX(-22deg) translate(8px,7px);z-index:-2}
.btn.ghost::before{background:transparent;border:1.5px solid var(--white)}
.btn.ghost::after{border-color:transparent;border-bottom:1.5px solid var(--white);border-left:1.5px solid var(--white)}
.arrow{width:20px;height:10px}
.site-header{top:0;height:96px;background:var(--white)}
.brand{position:absolute;display:flex;align-items:center;gap:10px;font-family:'Montserrat',sans-serif;font-weight:800;color:var(--blue-bright);text-transform:uppercase;white-space:nowrap}
.brand .dot{width:20px;height:20px;border-radius:50%;background:var(--blue-bright)}
.nav a{position:absolute;top:33px;font-size:15px;font-weight:500;color:#222;text-decoration:none}
.nav a.active{color:var(--blue-bright)}
.hero{top:96px;height:547px;background:linear-gradient(100deg,var(--blue-hero) 0%,#4A8FD5 55%,#3A82CC 100%)}
.hero h1{position:absolute;left:86px;top:88px;z-index:2;font-weight:800;font-size:54px;line-height:78px;letter-spacing:11px;color:var(--white);white-space:nowrap}
.dots-slider span{position:absolute;top:469px;height:4px;width:42px;background:rgba(255,255,255,.45)}
.dots-slider span.on{background:var(--white)}
.about{top:643px;height:542px}
.about p{position:absolute;left:612px;top:222px;width:502px;font-size:15.5px;line-height:27.5px;color:#444;text-align:justify}
.services{top:1185px;height:825px;background:var(--ink)}
.svc-card{position:absolute;top:210px;width:328px}
.svc-img{position:relative;width:328px;height:296px}
.svc-img .shape{position:absolute;inset:14px 0 0 0;border-radius:42% 58% 46% 54% / 48% 40% 60% 52%}
.svc-img svg{position:absolute;inset:0}
.svc-card h3{margin-top:18px;font-size:17px;font-weight:700;color:var(--white)}
.svc-card p{margin-top:14px;font-size:14.5px;line-height:25px;color:#c9c9d1}
.svc-card .more{display:flex;align-items:center;gap:6px;margin-top:14px;font-size:15px;font-weight:700;color:var(--blue-bright)}
.why{top:2010px;height:680px;background:var(--white)}
.feature{position:absolute;width:260px;padding-left:58px}
.feature svg{position:absolute;left:0;top:0;width:46px;height:42px}
.feature h4{font-size:15px;font-weight:700;color:#222}
.feature p{margin-top:8px;font-size:13.5px;line-height:20px;color:#555}
.gallery{top:2690px;height:780px;background:var(--ink)}
.strip{position:absolute;top:172px;height:565px}
.testimonials{top:3470px;height:610px;background:var(--white)}
.t-card{position:absolute;top:237px;width:329px;height:272px;background:var(--white);border-radius:6px;box-shadow:0 4px 22px rgba(20,40,80,.12);text-align:center;padding:58px 30px 0}
.t-card .avatar{position:absolute;left:124px;top:-44px;width:80px;height:80px;border-radius:50%;border:3px solid var(--white)}
.t-card h5{font-size:15px;font-weight:700;color:#222}
.stars{margin-top:8px;color:var(--star);font-size:18px;letter-spacing:3px}
.t-card p{margin-top:10px;font-size:14.5px;line-height:25px;font-style:italic;color:#444}
.contact{top:4080px;height:550px;background:var(--ink-2)}
.field{position:absolute;border-bottom:1.4px solid #5b5c66;color:var(--white);font-size:14.5px;display:flex;align-items:flex-end;gap:8px;padding-bottom:8px}
.field svg{width:14px;height:14px}
.site-footer{top:4630px;height:429px;background:var(--white)}
.f-head{position:absolute;top:118px;font-family:'Audiowide',sans-serif;font-style:italic;font-size:13px;color:var(--blue-bright);text-transform:uppercase}
.f-list{position:absolute;top:152px;list-style:none}
.f-list li{height:39px;font-size:14px;color:#333;display:flex;align-items:flex-start;gap:10px}
.f-list li::before{content:"→";color:#777}
.f-info{position:absolute;left:86px;font-size:14px;line-height:22px;color:#333;display:flex;gap:14px}
.f-info svg{width:16px;height:16px;margin-top:3px;flex:none}
.social{position:absolute;top:150px;width:32px;height:32px;border-radius:50%;background:var(--blue-bright)}
</style>
</head>
<body>

<header class="site-header">
  <div class="brand" style="left:86px;top:28px;font-size:21px;letter-spacing:1.5px"><span class="dot"></span>Rimcraft Works</div>
  <nav class="nav">
    <a class="active" style="left:378px">Home</a>
    <a style="left:460px">About</a>
    <a style="left:545px">Services</a>
    <a style="left:647px">Gallery</a>
    <a style="left:744px">Clients</a>
    <a style="left:836px">Contact</a>
  </nav>
  <a class="btn" style="left:928px;top:20px;width:178px;height:46px;font-size:15px">
    <svg width="14" height="14" viewBox="0 0 24 24" fill="#fff"><path d="M6.6 10.8a15 15 0 006.6 6.6l2.2-2.2a1 1 0 011-.25 11.4 11.4 0 003.6.6 1 1 0 011 1V20a1 1 0 01-1 1A17 17 0 013 4a1 1 0 011-1h3.5a1 1 0 011 1c0 1.25.2 2.45.6 3.6a1 1 0 01-.25 1z"/></svg>
    555-014-2968
  </a>
</header>

<section class="hero">
  <div class="photo" role="img" aria-label="Smiling technician in cap and overalls holding polished alloy wheels" style="left:455px;top:40px;width:665px;height:507px;border-radius:50% 50% 0 48% / 62% 58% 0 58%;background:radial-gradient(ellipse at 60% 40%,#8a8f97 0%,#5c616a 45%,#33363d 100%)"></div>
  <h1>WHEEL<br>REPAIRS<br>SPECIALISTS</h1>
  <a class="btn ghost" style="left:98px;top:349px;width:206px;height:46px;font-size:14px">Request a quote
    <svg class="arrow" viewBox="0 0 20 10" fill="none" stroke="#fff" stroke-width="1.6"><path d="M1 7c5-6 11-6 17 0M18 7l-4-1M18 7l-1-4"/></svg></a>
  <div class="dots-slider"><span class="on" style="left:84px"></span><span style="left:138px"></span><span style="left:194px"></span></div>
</section>

<section class="about">
  <div class="photo" role="img" aria-label="Mechanic fitting an alloy wheel onto a car" style="left:84px;top:33px;width:226px;height:254px;background:linear-gradient(135deg,#6d737b,#2f3238)"></div>
  <div class="abs" style="left:188px;top:133px;width:244px;height:245px;border:3px solid var(--blue-bright)"></div>
  <div class="photo" role="img" aria-label="Technician with crossed arms in front of a tyre rack" style="left:331px;top:256px;width:226px;height:254px;background:linear-gradient(160deg,#5d6470,#23262c)"></div>
  <div class="num abs" style="left:556px;top:117px">01</div>
  <div class="label abs" style="left:612px;top:150px;color:#222">About</div>
  <div class="display abs" style="left:612px;top:166px;font-size:36px">Rimcraft Works</div>
  <p>Lorem ipsum dolor sit amet, consecter adipiscing elit. Sed finibus interdum lorem, sit amet posuere velit consequat nec. Nulla quis sagittis augue, et bibendum turpis. Nunc suscipit urna magna, id tempor leo luctus vitae. Nunc quis mattis nibh, in feugiat velit. Donec vehicula pulvinar nulla at efficitur.</p>
  <a class="btn" style="left:622px;top:414px;width:180px;height:46px">Read More
    <svg class="arrow" viewBox="0 0 20 10" fill="none" stroke="#fff" stroke-width="1.6"><path d="M1 7c5-6 11-6 17 0M18 7l-4-1M18 7l-1-4"/></svg></a>
</section>

<section class="services">
  <div class="num abs" style="left:478px;top:55px">02</div>
  <div class="label abs" style="left:558px;top:92px;color:#fff">Service</div>
  <div class="display abs" style="left:0;width:1200px;top:108px;text-align:center;font-size:34px;line-height:38px">Experience our range<br>of services</div>

  <div class="svc-card" style="left:84px">
    <div class="svc-img">
      <div class="shape" role="img" aria-label="Gloved hand reworking the spokes of a wheel rim" style="background:radial-gradient(ellipse at 55% 45%,#8f7868,#4a3e37 55%,#1b1a1f)"></div>
      <svg viewBox="0 0 328 296" fill="none" stroke="var(--blue-bright)" stroke-width="2"><path d="M8 120C20 40 120 -2 230 6c60 6 94 52 96 90"/></svg>
    </div>
    <h3>Split Rim Re-builds</h3>
    <p>Nunc suscipit urna magna, id tempor leo luctus vitae. Nunc quis maibh, in feugiat velit.</p>
    <div class="more">Read More <svg class="arrow" viewBox="0 0 20 10" fill="none" stroke="var(--blue-bright)" stroke-width="1.6"><path d="M1 7c5-6 11-6 17 0M18 7l-4-1M18 7l-1-4"/></svg></div>
  </div>
  <div class="svc-card" style="left:436px">
    <div class="svc-img">
      <div class="shape" role="img" aria-label="Brush polishing the spokes of a silver alloy wheel" style="background:radial-gradient(ellipse at 50% 45%,#d6d8db,#8c9097 50%,#2c2e33)"></div>
      <svg viewBox="0 0 328 296" fill="none" stroke="var(--blue-bright)" stroke-width="2"><path d="M8 120C20 40 120 -2 230 6c60 6 94 52 96 90"/></svg>
    </div>
    <h3>Wheel polishing</h3>
    <p>Nunc suscipit urna magna, id tempor leo luctus vitae. Nunc quis maibh, in feugiat velit.</p>
    <div class="more">Read More <svg class="arrow" viewBox="0 0 20 10" fill="none" stroke="var(--blue-bright)" stroke-width="1.6"><path d="M1 7c5-6 11-6 17 0M18 7l-4-1M18 7l-1-4"/></svg></div>
  </div>
  <div class="svc-card" style="left:787px">
    <div class="svc-img">
      <div class="shape" role="img" aria-label="Cloth wiping a dark alloy wheel after flatspot removal" style="background:radial-gradient(ellipse at 50% 45%,#9ea3aa,#4f545c 50%,#1f2126)"></div>
      <svg viewBox="0 0 328 296" fill="none" stroke="var(--blue-bright)" stroke-width="2"><path d="M8 120C20 40 120 -2 230 6c60 6 94 52 96 90"/></svg>
    </div>
    <h3>Buckle &amp; Flatspot Removal</h3>
    <p>Nunc suscipit urna magna, id tempor leo luctus vitae. Nunc quis maibh, in feugiat velit.</p>
    <div class="more">Read More <svg class="arrow" viewBox="0 0 20 10" fill="none" stroke="var(--blue-bright)" stroke-width="1.6"><path d="M1 7c5-6 11-6 17 0M18 7l-4-1M18 7l-1-4"/></svg></div>
  </div>

  <a class="btn" style="left:486px;top:715px;width:220px;height:46px">View All Services
    <svg class="arrow" viewBox="0 0 20 10" fill="none" stroke="#fff" stroke-width="1.6"><path d="M1 7c5-6 11-6 17 0M18 7l-4-1M18 7l-1-4"/></svg></a>
</section>

<section class="why">
  <div class="label abs" style="left:86px;top:94px;color:#222">Why us</div>
  <div class="num abs" style="left:190px;top:52px">03</div>
  <div class="display abs" style="left:86px;top:112px;font-size:34px;line-height:38px">Something to make<br>you love more</div>

  <div class="feature" style="left:86px;top:220px">
    <svg viewBox="0 0 46 42" fill="none" stroke="var(--blue-bright)" stroke-width="2"><path d="M2 14l8-4 8 3 6-3 8 2 12 2M4 14l6 14 10 6 8-2 10-8 6-10M18 16l6 4 6-2"/></svg>
    <h4>Trusted by clients</h4><p>Lorem ipsum dolor sit amet, conser adipiscing elit.</p></div>
  <div class="feature" style="left:360px;top:220px">
    <svg viewBox="0 0 46 42" fill="none" stroke="var(--blue-bright)" stroke-width="2"><path d="M8 24v-6a14 14 0 0128 0v6"/><rect x="4" y="22" width="8" height="12" rx="2"/><rect x="32" y="22" width="8" height="12" rx="2"/><path d="M36 34c0 4-4 6-10 6"/></svg>
    <h4>Premium Support</h4><p>Lorem ipsum dolor sit amet, conser adipiscing elit.</p></div>
  <div class="feature" style="left:86px;top:354px">
    <svg viewBox="0 0 46 42" fill="none" stroke="var(--blue-bright)" stroke-width="2"><circle cx="22" cy="12" r="9"/><path d="M18 12l3 3 5-6M14 20l-4 14 6-2 4 5 2-12M30 20l4 14-6-2-4 5"/></svg>
    <h4>High quality service</h4><p>Lorem ipsum dolor sit amet, conser adipiscing elit.</p></div>
  <div class="feature" style="left:360px;top:354px">
    <svg viewBox="0 0 46 42" fill="none" stroke="var(--blue-bright)" stroke-width="2"><rect x="6" y="6" width="30" height="24" rx="3"/><path d="M6 14h30M12 22h8"/><circle cx="34" cy="30" r="8"/><path d="M30 30l3 3 5-5"/></svg>
    <h4>No prepayment required</h4><p>Lorem ipsum dolor sit amet, conser adipiscing elit.</p></div>
  <div class="feature" style="left:86px;top:484px">
    <svg viewBox="0 0 46 42" fill="none" stroke="var(--blue-bright)" stroke-width="2"><circle cx="23" cy="12" r="7"/><path d="M10 38v-6a13 13 0 0126 0v6"/><circle cx="8" cy="18" r="4"/><circle cx="38" cy="18" r="4"/><path d="M2 34a6 6 0 016-8M44 34a6 6 0 00-6-8"/></svg>
    <h4>Technical Staff</h4><p>Lorem ipsum dolor sit amet, conser adipiscing elit.</p></div>
  <div class="feature" style="left:360px;top:484px">
    <svg viewBox="0 0 46 42" fill="none" stroke="var(--blue-bright)" stroke-width="2"><circle cx="20" cy="20" r="16"/><path d="M20 10v10l6 4"/><circle cx="32" cy="32" r="7" fill="var(--blue-bright)"/><path d="M29 32l2 2 4-4" stroke="#fff"/></svg>
    <h4>On time Delivery</h4><p>Lorem ipsum dolor sit amet, conser adipiscing elit.</p></div>

  <div class="photo" role="img" aria-label="Mechanic in blue overalls kneeling beside a new tyre and alloy wheel" style="left:700px;top:0;width:412px;height:680px;background:linear-gradient(180deg,#3a7fcf 0%,#8fb9e4 35%,#ffffff 72%)"></div>
  <div class="photo" role="img" aria-label="Mechanic figure and tyre" style="left:696px;top:20px;width:400px;height:620px;border-radius:45% 45% 20% 20%;background:radial-gradient(ellipse at 55% 55%,#2f3440 0%,#1e4f9c 45%,rgba(30,80,160,0) 72%)"></div>
</section>

<section class="gallery">
  <svg class="abs" style="left:90px;top:66px" width="140" height="30" viewBox="0 0 140 30" fill="var(--blue-bright)">
    <g id="dotrow"><circle cx="3" cy="3" r="2"/><circle cx="19" cy="3" r="2"/><circle cx="35" cy="3" r="2"/><circle cx="51" cy="3" r="2"/><circle cx="67" cy="3" r="2"/><circle cx="83" cy="3" r="2"/><circle cx="99" cy="3" r="2"/><circle cx="115" cy="3" r="2"/><circle cx="131" cy="3" r="2"/></g>
    <use href="#dotrow" y="11"/><use href="#dotrow" y="22"/>
  </svg>
  <div class="num abs" style="left:452px;top:62px">04</div>
  <div class="label abs" style="left:552px;top:96px;color:#fff">Gallery</div>
  <div class="display abs" style="left:0;width:1200px;top:113px;text-align:center;font-size:34px">Our latest work</div>

  <div class="photo strip" role="img" aria-label="Close-up of a multi-spoke alloy wheel in black and white" style="left:0;width:139px;background:linear-gradient(180deg,#4a4d52,#b9bcc0 50%,#3a3c40)"></div>
  <div class="photo strip" role="img" aria-label="Technician inspecting a tyre in black and white" style="left:139px;width:140px;background:linear-gradient(180deg,#7d8085,#3d4044 60%,#1c1d20)"></div>
  <div class="photo strip" role="img" aria-label="Alloy wheel and tyre standing on wet ground at sunset" style="left:279px;width:499px;background:radial-gradient(ellipse at 50% 40%,#f1a15c 0%,#b4592f 35%,#3b2420 70%,#151315 100%)"></div>
  <div class="photo strip" role="img" aria-label="Dark wheel hub detail in black and white" style="left:778px;width:140px;background:linear-gradient(180deg,#2a2b2e,#6c6f74 50%,#1b1c1f)"></div>
  <div class="photo strip" role="img" aria-label="Five-spoke alloy wheel face in black and white" style="left:918px;width:141px;background:linear-gradient(180deg,#1a1a1c,#d8d9db 45%,#8b8e93 70%,#1c1d20)"></div>
  <div class="photo strip" role="img" aria-label="Silver spoked rim in black and white" style="left:1059px;width:141px;background:linear-gradient(180deg,#9a9da1,#e0e1e3 45%,#55585d)"></div>
</section>

<section class="testimonials">
  <div class="label abs" style="left:86px;top:63px;color:#222">Testimonials</div>
  <div class="num abs" style="left:285px;top:22px">05</div>
  <div class="display abs" style="left:86px;top:79px;font-size:34px;line-height:38px">What client say<br>about us</div>
  <a class="btn" style="left:918px;top:82px;width:190px;height:46px">View All
    <svg class="arrow" viewBox="0 0 20 10" fill="none" stroke="#fff" stroke-width="1.6"><path d="M1 7c5-6 11-6 17 0M18 7l-4-1M18 7l-1-4"/></svg></a>

  <div class="t-card" style="left:84px">
    <div class="avatar" role="img" aria-label="Portrait of client Jhon Doe" style="background:linear-gradient(160deg,#9fa6b0,#4b5361)"></div>
    <h5>Jhon Doe</h5><div class="stars">★★★★★</div>
    <p>Aliquam lacinia erat, eu accumsan sapien fermtum sed. Cras placerat augue euismod tellus malesuada, quis porta lorem porta. Nunc a eleifend nisl.</p></div>
  <div class="t-card" style="left:435px">
    <div class="avatar" role="img" aria-label="Portrait of client Olivia W." style="background:linear-gradient(160deg,#e3e6ea,#5a6270)"></div>
    <h5>Olivia W.</h5><div class="stars">★★★★★</div>
    <p>Aliquam lacinia erat, eu accumsan sapien fermtum sed. Cras placerat augue euismod tellus malesuada, quis porta lorem porta. Nunc a eleifend nisl.</p></div>
  <div class="t-card" style="left:785px">
    <div class="avatar" role="img" aria-label="Portrait of client Lukas Wilson" style="background:linear-gradient(160deg,#d7dade,#6b7380)"></div>
    <h5>Lukas Wilson</h5><div class="stars">★★★★★</div>
    <p>Aliquam lacinia erat, eu accumsan sapien fermtum sed. Cras placerat augue euismod tellus malesuada, quis porta lorem porta. Nunc a eleifend nisl.</p></div>
</section>

<section class="contact">
  <div class="photo" role="img" aria-label="Mechanic tightening wheel bolts with a yellow impact wrench" style="left:0;top:0;width:480px;height:550px;background:radial-gradient(ellipse at 40% 55%,#6b5a44 0%,#332c26 45%,#1a1b20 100%)"></div>
  <div class="num abs" style="left:460px;top:56px">06</div>
  <div class="label abs" style="left:522px;top:90px;color:#fff">Contact us</div>
  <div class="display abs" style="left:522px;top:106px;font-size:34px;line-height:40px">Get in touch</div>

  <div class="field" style="left:522px;top:164px;width:286px;height:34px">
    <svg viewBox="0 0 14 14" fill="#9a9aa3"><circle cx="7" cy="4" r="3"/><path d="M1 14a6 6 0 0112 0z"/></svg>Name</div>
  <div class="field" style="left:830px;top:164px;width:288px;height:34px">
    <svg viewBox="0 0 24 24" fill="#9a9aa3"><path d="M6.6 10.8a15 15 0 006.6 6.6l2.2-2.2a1 1 0 011-.25 11.4 11.4 0 003.6.6 1 1 0 011 1V20a1 1 0 01-1 1A17 17 0 013 4a1 1 0 011-1h3.5a1 1 0 011 1c0 1.25.2 2.45.6 3.6a1 1 0 01-.25 1z"/></svg>Phone</div>
  <div class="field" style="left:522px;top:230px;width:596px;height:34px">
    <svg viewBox="0 0 14 14" fill="#9a9aa3"><rect x="0" y="2" width="14" height="10" rx="1"/></svg>Email</div>
  <div class="field" style="left:522px;top:288px;width:596px;height:84px;align-items:flex-start;padding-top:0">
    <svg viewBox="0 0 14 14" fill="#9a9aa3"><path d="M1 13l1-4 8-8 3 3-8 8z"/></svg>Your Message</div>

  <a class="btn" style="left:530px;top:403px;width:192px;height:46px">Submit Now
    <svg class="arrow" viewBox="0 0 20 10" fill="none" stroke="#fff" stroke-width="1.6"><path d="M1 7c5-6 11-6 17 0M18 7l-4-1M18 7l-1-4"/></svg></a>
</section>

<footer class="site-footer">
  <div class="brand" style="left:90px;top:128px;font-size:22px;letter-spacing:1.5px"><span class="dot"></span>Rimcraft Works</div>
  <div class="f-info" style="top:192px">
    <svg viewBox="0 0 16 16" fill="var(--blue-bright)"><path d="M8 0a6 6 0 016 6c0 4-6 10-6 10S2 10 2 6a6 6 0 016-6zm0 3.5a2.5 2.5 0 100 5 2.5 2.5 0 000-5z"/></svg>
    <div>42 Orchard Lane<br>Fairview PA 10000</div></div>
  <div class="f-info" style="top:256px">
    <svg viewBox="0 0 16 16" fill="var(--blue-bright)"><path d="M0 3h16v10H0z" opacity=".9"/><path d="M0 3l8 6 8-6" stroke="#fff" fill="none"/></svg>
    <div>hello@rimcraftworks.com</div></div>
  <div class="f-info" style="top:296px">
    <svg viewBox="0 0 24 24" fill="var(--blue-bright)"><path d="M6.6 10.8a15 15 0 006.6 6.6l2.2-2.2a1 1 0 011-.25 11.4 11.4 0 003.6.6 1 1 0 011 1V20a1 1 0 01-1 1A17 17 0 013 4a1 1 0 011-1h3.5a1 1 0 011 1c0 1.25.2 2.45.6 3.6a1 1 0 01-.25 1z"/></svg>
    <div>555-014-2968</div></div>

  <div class="f-head" style="left:450px">Quick Links</div>
  <ul class="f-list" style="left:450px"><li>Home</li><li>About</li><li>Services</li><li>Gallery</li><li>Clients</li><li>Contact</li></ul>

  <div class="f-head" style="left:665px">Our Services</div>
  <ul class="f-list" style="left:665px"><li>Split Rim Re-builds</li><li>Wheel polishing</li><li>Buckle &amp; Flatspot Removal</li><li>Alloys &amp; Colour Change</li><li>Wheel Diamond Cutting</li></ul>

  <div class="f-head" style="left:945px">Follow Us</div>
  <span class="social" style="left:949px"></span>
  <span class="social" style="left:993px"></span>
  <span class="social" style="left:1037px"></span>
  <span class="social" style="left:1081px"></span>

  <div class="abs" style="left:1060px;top:280px;width:56px;height:56px;border-radius:50%;background:var(--blue-bright);display:flex;align-items:center;justify-content:center">
    <svg width="26" height="14" viewBox="0 0 26 14" fill="none" stroke="#fff" stroke-width="2"><path d="M2 12L13 2l11 10"/></svg></div>

  <div class="abs" style="left:86px;top:392px;font-size:13.5px;color:#333">© 2023 <span style="color:var(--blue-bright)">Rimcraft Works</span>. All right reserved</div>
</footer>

</body>
</html>
```